Hi, Looking for an upgraded business card to the aged one attached. Open to suggestions and no real limitations, but if your going to use a picture of a taxi i think it should be vector based rather than a full color picture. I've uploaded a 2 pictures of the type of taxi which is a Torvane K5 in white. The taxi markings look like the pink one in the picture but to be clear his is white. The taxi is in Bermuda so if you wanted to include something island based that's ok as well but not required. The other thing he wanted to keep on there was the Harbour Watch, with the retired police office incorporated somehow.

Requirements
Must have
• Bermuda Taxi Operator
Retired Police Officer
Police Crest
Taxi #
Email
Mobile Number

```html
<!DOCTYPE html>
<html lang="en">
<head>
<meta charset="utf-8">
<title>Bermuda Taxi Operator – Business Card</title>
<link href="https://fonts.googleapis.com/css2?family=Roboto:wght@300;400;500&display=swap" rel="stylesheet">
<style>
  :root {
    --page: #e4e4e2;
    --card: #2c2c2d;
    --card-edge: #1f5aa6;
    --accent: #2a63b8;
    --ink: #ffffff;
    --ink-soft: #d6d6d6;
    --rule: #cfcfcf;
    --faint: #6a6a6c;
  }
  * { box-sizing: border-box; margin: 0; padding: 0; }
  html, body { width: 1200px; height: 801px; overflow: hidden; }
  body {
    background: var(--page);
    font-family: "Roboto", Arial, sans-serif;
    position: relative;
  }
  .card {
    position: absolute;
    top: 246px;
    width: 540px;
    height: 309px;
    background: var(--card);
    border-bottom: 3px solid var(--card-edge);
    overflow: hidden;
  }
  .card--front { left: 40px; }
  .card--back { left: 620px; }

  /* Front */
  .front__title {
    position: absolute; left: 34px; top: 40px;
    color: var(--ink); font-weight: 500; font-size: 19px; letter-spacing: 0.3px;
  }
  .mark {
    position: absolute; display: flex; align-items: center; gap: 10px;
    color: var(--ink); font-weight: 500;
  }
  .mark__dot { border-radius: 50%; background: var(--accent); flex: none; }
  .front__mark { right: 30px; top: 26px; font-size: 17px; }
  .front__mark .mark__dot { width: 22px; height: 22px; }
  .front__rule {
    position: absolute; left: 34px; right: 30px; top: 138px;
    height: 1px; background: var(--rule);
  }
  .front__taxi-no {
    position: absolute; right: 30px; top: 152px;
    color: var(--ink-soft); font-weight: 300; font-size: 15px;
  }
  .person { position: absolute; left: 34px; top: 166px; }
  .person__name { color: var(--accent); font-weight: 500; font-size: 21px; }
  .person__role { color: var(--ink-soft); font-weight: 400; font-size: 16px; margin-top: 2px; }
  .person__rule { width: 220px; height: 1px; background: var(--rule); margin: 12px 0 12px; }
  .contact { list-style: none; }
  .contact__item {
    display: flex; align-items: center; gap: 12px;
    color: var(--ink-soft); font-weight: 300; font-size: 15px; margin-bottom: 6px;
  }
  .contact__icon { width: 13px; height: 13px; fill: none; stroke: var(--accent); stroke-width: 1.6; }

  /* Back */
  .back__photo {
    position: absolute; left: 0; top: 0; width: 300px; height: 100%;
    background: linear-gradient(160deg, #c9b9b4 0%, #a99a96 30%, #d86fa8 55%, #8b8a88 78%, #6f6f6e 100%);
  }
  .back__fade {
    position: absolute; left: 150px; top: 0; width: 200px; height: 100%;
    background: linear-gradient(90deg, rgba(44,44,45,0) 0%, var(--card) 100%);
  }
  .back__mark { right: 40px; top: 90px; font-size: 22px; color: var(--faint); }
  .back__mark .mark__dot { width: 40px; height: 40px; background: var(--faint); }
  .back__title {
    position: absolute; right: 28px; bottom: 34px;
    color: var(--ink); font-weight: 500; font-size: 18px; letter-spacing: 0.3px;
  }
</style>
</head>
<body>
  <section class="card card--front">
    <h1 class="front__title">BERMUDA TAXI OPERATOR</h1>
    <div class="mark front__mark"><span class="mark__dot"></span>Harbour Watch</div>
    <div class="front__rule"></div>
    <p class="front__taxi-no">Taxi #T2417</p>
    <div class="person">
      <p class="person__name">Marcus Delane</p>
      <p class="person__role">Retired Police Officer</p>
      <div class="person__rule"></div>
      <ul class="contact">
        <li class="contact__item">
          <svg class="contact__icon" viewBox="0 0 14 14"><path d="M3 1 L5 4 L4 6 Q6 9 8 10 L10 9 L13 11 L12 13 Q5 13 1 3 Z" fill="#2a63b8" stroke="none"/></svg>
          1-441-555-0142
        </li>
        <li class="contact__item">
          <svg class="contact__icon" viewBox="0 0 14 14"><rect x="1" y="3" width="12" height="8"/><path d="M1 3 L7 8 L13 3"/></svg>
          mdelane@mailbox.com
        </li>
      </ul>
    </div>
  </section>

  <section class="card card--back">
    <div class="back__photo" role="img" aria-label="Photo of a pink taxi van parked at a kerb on a Bermuda street with pastel buildings behind"></div>
    <div class="back__fade"></div>
    <div class="mark back__mark"><span class="mark__dot"></span>Harbour Watch</div>
    <h2 class="back__title">BERMUDA TAXI OPERATOR</h2>
  </section>
</body>
</html>
```